Postcard Design - New Movers - Men only haircuts

Advertisement for "New Movers" into the local area. to try our hair curt facility. Our business is called Shearing Den; hair cuts for men and boys and can be found on FB using the words "Shearing Den, Pooler Georgia". Our décor is man cave.

Industry/Entity Type

Hair

```html
<!DOCTYPE html>
<html lang="en">
<head>
<meta charset="utf-8">
<title>Shearing Den – Men and Boys Haircuts</title>
<link rel="stylesheet" href="https://fonts.googleapis.com/css2?family=Kaushan+Script&family=Roboto+Condensed:wght@300;400;700&display=swap">
<style>
  :root {
    --page: #ffffff;
    --bar-dark: #111111;
    --bar-mid: #3a3a3c;
    --panel: #b3b29c;
    --ink: #3a3a3a;
    --body-ink: #3f3f3f;
    --yellow: #f5e61c;
    --cream: #d8d5bc;
    --khaki: #bab89f;
    --band: #000000;
    --band-edge: #2b2b2b;
    --hair-dark: #3b2a1a;
    --hair-light: #a98b62;
    --skin: #d6b39a;
  }
  * { margin: 0; padding: 0; box-sizing: border-box; }
  html, body { width: 1200px; height: 930px; overflow: hidden; background: var(--page); }
  .postcard { position: relative; width: 1200px; height: 930px; font-family: "Roboto Condensed", sans-serif; }

  .top-bar {
    position: absolute; left: 30px; top: 30px; width: 1140px; height: 118px;
    background: linear-gradient(180deg, var(--bar-mid) 0%, var(--bar-dark) 100%);
  }
  .top-bar__title {
    position: absolute; left: 83px; top: 36px;
    font-weight: 300; font-size: 39px; letter-spacing: 0; color: var(--cream);
  }
  .top-bar__stylist {
    position: absolute; right: 34px; top: 40px;
    font-family: "Kaushan Script", cursive; font-size: 31px; line-height: 40px; color: var(--yellow);
    white-space: nowrap;
  }

  .hero-photo {
    position: absolute; left: 30px; top: 148px; width: 567px; height: 752px;
    background:
      radial-gradient(ellipse 60% 45% at 45% 75%, var(--skin) 0%, rgba(214,179,154,0) 70%),
      linear-gradient(170deg, var(--hair-dark) 0%, var(--hair-light) 35%, #c9a98c 60%, #f2efea 100%);
  }

  .services {
    position: absolute; left: 597px; top: 148px; width: 573px; height: 609px;
    background: var(--panel);
  }
  .service { position: absolute; left: 65px; width: 500px; }
  .service--cut { top: 56px; }
  .service--beard { top: 190px; }
  .service--kids { top: 348px; }
  .service__title {
    font-weight: 700; font-size: 35px; line-height: 36px; color: var(--ink);
    white-space: nowrap;
  }
  .service__text {
    font-size: 22px; line-height: 29px; color: var(--body-ink); letter-spacing: 0.2px;
    white-space: nowrap;
  }

  .step-badge { position: absolute; left: 558px; width: 80px; height: 80px; }
  .step-badge--1 { top: 197px; }
  .step-badge--2 { top: 340px; }
  .step-badge--3 { top: 487px; }

  .call {
    position: absolute; left: 710px; top: 662px; color: var(--cream); white-space: nowrap;
  }
  .call__word { font-weight: 700; font-size: 40px; color: var(--yellow); vertical-align: top; line-height: 44px; }
  .call__note { font-size: 21px; letter-spacing: 1px; margin-left: 10px; vertical-align: top; line-height: 32px; color: #eeeadb; }
  .call__phone {
    position: absolute; left: 710px; top: 704px; white-space: nowrap;
    font-weight: 700; font-size: 40px; letter-spacing: 8.5px; color: var(--ink);
  }

  .footer-band {
    position: absolute; left: 597px; top: 757px; width: 573px; height: 143px;
    background: var(--band); border-top: 11px solid var(--band-edge);
    text-align: center;
  }
  .footer-band__name {
    margin-top: 20px; font-size: 54px; line-height: 60px; color: var(--khaki); font-weight: 400;
  }
  .footer-band__address {
    margin-top: 17px; font-weight: 700; font-size: 21px; letter-spacing: 0.4px; color: var(--khaki);
    white-space: nowrap;
  }
</style>
</head>
<body>
<div class="postcard">
  <header class="top-bar">
    <h1 class="top-bar__title">MEN AND BOYS HAIRCUTS</h1>
    <p class="top-bar__stylist">Stylist Dana Reed</p>
  </header>

  <div class="hero-photo" role="img" aria-label="Portrait photo of a young man with shaggy layered brown hair"></div>

  <section class="services">
    <div class="service service--cut">
      <h2 class="service__title">HAIRCUT &amp; STYLE</h2>
      <p class="service__text">Every haircut is executed with precision and style.<br>We promise you'll walk out of here lookin' fresh.</p>
    </div>
    <div class="service service--beard">
      <h2 class="service__title">BEARD OR MOUSTACHE TRIM</h2>
      <p class="service__text">Beards and moustaches are in. We will make sure<br>your burly friend is tamed and styled to look better<br>than ever.</p>
    </div>
    <div class="service service--kids">
      <h2 class="service__title">KIDS CUTS</h2>
      <p class="service__text">We offer a fun experience for our Den kids. We<br>cut kids hair in a race car chair that has lights,<br>horn, and wheel that turns. After the cut they will<br>get to pick a toy from our treasure chest.</p>
    </div>
  </section>

  <svg class="step-badge step-badge--1" viewBox="0 0 80 80" aria-hidden="true">
    <circle cx="40" cy="41" r="36" fill="#000" opacity="0.25"/>
    <circle cx="40" cy="39" r="36" fill="#fff"/>
    <circle cx="40" cy="39" r="30" fill="var(--yellow)"/>
    <text x="40" y="50" text-anchor="middle" font-family="Roboto Condensed, sans-serif" font-weight="700" font-size="32" fill="#fff">1</text>
  </svg>
  <svg class="step-badge step-badge--2" viewBox="0 0 80 80" aria-hidden="true">
    <circle cx="40" cy="41" r="36" fill="#000" opacity="0.25"/>
    <circle cx="40" cy="39" r="36" fill="#fff"/>
    <circle cx="40" cy="39" r="30" fill="var(--yellow)"/>
    <text x="40" y="50" text-anchor="middle" font-family="Roboto Condensed, sans-serif" font-weight="700" font-size="32" fill="#fff">2</text>
  </svg>
  <svg class="step-badge step-badge--3" viewBox="0 0 80 80" aria-hidden="true">
    <circle cx="40" cy="41" r="36" fill="#000" opacity="0.25"/>
    <circle cx="40" cy="39" r="36" fill="#fff"/>
    <circle cx="40" cy="39" r="30" fill="var(--yellow)"/>
    <text x="40" y="50" text-anchor="middle" font-family="Roboto Condensed, sans-serif" font-weight="700" font-size="32" fill="#fff">3</text>
  </svg>

  <p class="call"><span class="call__word">CALL</span><span class="call__note">FOR MORE INFORMATION:</span></p>
  <p class="call__phone">(912)555-0148</p>

  <footer class="footer-band">
    <p class="footer-band__name">Shearing Den</p>
    <p class="footer-band__address">2250 W MARKET BLVD UNIT #120, BRAYFIELD, GA 30999</p>
  </footer>
</div>
</body>
</html>
```